Build With Sisters, 2019 Save The Date

Please develop a save the date flyer our 4th Annual Build With Sisters and See Them Soar! This event is focused on maintaining participation and appreciation for women in the design and construction industry.

This unique Forum provides a venue to engage everyone from executives to those just beginning their careers with active, hands-on sessions and vibrant networking with the best and brightest in the A/E/C industry. In our usual Q-MarTO Forum style, Keynotes become table participants and table participants become presenters, encouraging participants to assimilate what they are learning. Join local, state and national leaders and subject matter experts as we candidly explore and address the issues affecting women in our industry.

Industry/Entity Type

Construction

Font styles to use
Sans Serif

Requirements
Must have
• This is a save the date, Must have:
• Q-MarTO Logo
• Title: 4th Annual Build With Sisters and See Them Soar!
• Date: January 25, 2019
• Location: Bluestem Ridge Resort and Spa, San Marcos, TX
Nice to have
• A header that can easily be pulled to add to other marketing materials and for use across other platforms (web, etc.).

```html
<!DOCTYPE html>
<html lang="en">
<head>
<meta charset="utf-8">
<title>Build With Sisters – Save The Date</title>
<link rel="stylesheet" href="https://fonts.googleapis.com/css2?family=Montserrat+Alternates:wght@500;600&family=Questrial&family=Open+Sans:wght@500&display=swap">
<style>
  :root {
    --royal: #22459c;
    --royal-deep: #1c3a8a;
    --leaf: #8db43e;
    --ink: #3d3d3d;
    --slate: #4a4a4a;
    --paper: #ffffff;
    --lavender: #8e92c9;
    --night: #1e2b52;
  }
  * { margin: 0; padding: 0; box-sizing: border-box; }
  html, body { width: 848px; height: 1200px; overflow: hidden; }
  body { background: var(--paper); }
  .flyer {
    position: relative;
    width: 848px;
    height: 1200px;
    overflow: hidden;
    background: linear-gradient(30deg, var(--lavender) 0%, #c9cbe7 30%, #f4f4fb 60%, var(--paper) 80%);
  }
  .art { position: absolute; inset: 0; width: 848px; height: 1200px; }
  .headline {
    position: absolute;
    left: 0; width: 848px;
    text-align: center;
    font-family: "Montserrat Alternates", sans-serif;
    line-height: 1;
    white-space: nowrap;
  }
  .edition { top: 558px; font-size: 88px; font-weight: 600; color: var(--royal); letter-spacing: -1px; }
  .edition sup { font-size: 48px; vertical-align: 32px; margin-right: 30px; }
  .tagline { top: 661px; font-size: 40px; font-weight: 500; color: var(--ink); }
  .slogan { top: 705px; font-size: 84px; font-weight: 600; color: var(--leaf); letter-spacing: -1px; }
  .date-pill {
    position: absolute;
    left: 171px; top: 807px; width: 510px; height: 69px;
    border-radius: 14px;
    background: linear-gradient(180deg, #4a5fb0 0%, var(--royal) 50%, var(--royal-deep) 100%);
    color: var(--paper);
    font-family: "Montserrat Alternates", sans-serif;
    font-weight: 500;
    font-size: 52px;
    line-height: 1;
    display: flex; align-items: center; justify-content: center;
    word-spacing: 8px;
    white-space: nowrap;
  }
  .venue {
    position: absolute;
    left: 0; top: 884px; width: 848px;
    text-align: center;
    font-family: "Montserrat Alternates", sans-serif;
    font-weight: 500;
    font-size: 30px;
    line-height: 38px;
    color: var(--ink);
  }
  .brand-mark {
    position: absolute;
    left: 165px; top: 994px;
    width: 148px; height: 148px;
    border-radius: 50%;
    background: var(--royal);
  }
  .brand-name {
    position: absolute;
    left: 349px; top: 998px;
    font-family: "Questrial", sans-serif;
    font-size: 82px;
    color: var(--slate);
    line-height: 1;
    white-space: nowrap;
  }
  .brand-rule {
    position: absolute;
    left: 351px; top: 1084px; width: 328px; height: 2px;
    background: var(--slate);
  }
  .brand-sub {
    position: absolute;
    left: 353px; top: 1096px;
    font-family: "Open Sans", sans-serif;
    font-weight: 500;
    font-size: 20px;
    line-height: 1.2;
    color: var(--leaf);
    white-space: nowrap;
  }
</style>
</head>
<body>
  <main class="flyer">
    <svg class="art" viewBox="0 0 848 1200">
      <g class="accents">
        <polygon points="0,170 60,85 100,236" fill="var(--royal)"/>
        <polygon points="0,205 18,205 40,282 0,280" fill="var(--royal)"/>
        <polygon points="0,232 28,240 14,265" fill="var(--royal)"/>
        <polygon points="5,368 77,309 77,396" fill="var(--royal)"/>
        <polygon points="60,342 104,334 89,386" fill="var(--leaf)"/>
        <polygon points="0,398 21,428 0,432" fill="var(--leaf)"/>
        <polygon points="696,42 812,0 787,142" fill="var(--leaf)"/>
        <polygon points="790,43 836,20 838,68" fill="var(--royal)"/>
        <polygon points="685,112 733,113 706,156" fill="var(--royal)"/>
        <polygon points="763,145 820,211 782,223" fill="var(--royal)"/>
        <polygon points="802,152 848,120 848,172" fill="var(--leaf)"/>
      </g>
      <circle class="hero-ring" cx="448" cy="322" r="230" fill="none" stroke="var(--royal)" stroke-width="13"/>
      <defs>
        <radialGradient id="heroFill" cx="50%" cy="40%" r="60%">
          <stop offset="0%" stop-color="#3a4c7e"/>
          <stop offset="100%" stop-color="var(--night)"/>
        </radialGradient>
      </defs>
      <circle class="hero-photo" cx="448" cy="322" r="215" fill="url(#heroFill)" role="img" aria-label="Photo of a confident businesswoman in a dark suit, arms crossed, in front of a city skyline at dusk"/>
      <path class="hero-base" d="M137,519 Q446,366 754,519 Q446,580 137,519 Z" fill="var(--leaf)"/>
    </svg>

    <h1 class="headline edition">4<sup>th</sup>Annual</h1>
    <p class="headline tagline">Build With Sisters &amp; See</p>
    <p class="headline slogan">Them Soar!</p>

    <div class="date-pill">January 25, 2019</div>

    <p class="venue">Bluestem Ridge Resort and<br>Spa, San Marcos, TX</p>

    <div class="brand-mark"></div>
    <div class="brand-name">Q-MarTO</div>
    <div class="brand-rule"></div>
    <div class="brand-sub">Quarry Institute for Trades Operations</div>
  </main>
</body>
</html>
```